Swatch Flyer

My business is as owner and manager of 6 holiday lets in the South West of WA in the wine region.
All our properties are on rural bush locations, but close to all the amenitiies of the Tarrabellup township and major wineries in the area.
we advertise all the properties thru lodgio.com.au
you can check out the details of all the properties with the following links
www.lodgio.com.au/55841 Wattles Retreat..Max occ 16
www.lodgio.com.au/61673 Emberlight Retreat Max occ 8
www.lodgio.com.au/66777 Quokkas Corner Max occ 12
www.lodgio.com.au/93104 Bellintary Max occ 10
www.lodgio.com.au/135790 The Glade Retreat Max occ 8
www.lodgio.com.au/147300 Ferncliff Studio Max Occ 4
i am looking to produce a flyer that i can leave in all the houses to promote one to the other.
**I would like the flyer to be DL size (pls ignore the A5 mentioned above).
DL (99 x 210 mm) - Please download the templates below:
Photoshop - http://printnook.com.au/propath/download-template.aspx?Log=1&path=propath&pfid=BFB&pf_id=BFB&type=2
Illustrator - http://printnook.com.au/propath/download-template.aspx?Log=1&path=propath&pfid=BFB&pf_id=BFB&type=3
Thanks for all the submissions, but we are happy with one designer and just about to compete the process.
Target Market(s)
Family groups on holidays
Industry/Entity Type
Business
Requirements
Must have
- Photos and descriptions of all the houses.
Must have a feel of holidays in the wine region
You can get from the links I have given .
Also must have the logo and personal details as used on the business card

```html
<!DOCTYPE html>
<html lang="en">
<head>
<meta charset="utf-8">
<title>Lodgio Swatch Flyer</title>
<link href="https://fonts.googleapis.com/css2?family=Arimo:wght@400;700&display=swap" rel="stylesheet">
<style>
  :root{
    --page:#e9e9e9;
    --paper:#ffffff;
    --sky-top:#8fd3f4;
    --sky-bottom:#3fa9dd;
    --panel:#000000;
    --divider:#ffffff;
    --badge:#5fb336;
    --badge-ring:#ffffff;
    --ink-light:#ffffff;
    --ink-dark:#000000;
  }
  *{box-sizing:border-box;margin:0;padding:0}
  html,body{width:900px;height:1200px;overflow:hidden}
  body{background:var(--page);font-family:"Arimo",Arial,sans-serif;position:relative}

  .flyer{position:absolute;left:20px;top:295px;width:860px;height:610px;background:var(--paper);
    box-shadow:0 2px 6px rgba(0,0,0,.15);overflow:hidden}

  .topbar{position:absolute;left:0;top:0;width:100%;height:37px;
    background:linear-gradient(var(--sky-top),var(--sky-bottom))}
  .topbar__url{position:absolute;right:14px;top:10px;color:var(--ink-light);font-weight:700;font-size:15px;letter-spacing:.2px}

  .hero{position:absolute;left:0;top:37px;width:100%;height:221px;
    background:linear-gradient(180deg,#cfd9d6 0%,#b9c7b4 22%,#6f8f55 40%,#2fb1e4 58%,#1e9fd8 100%)}

  .brand{position:absolute;left:0;top:0;width:215px;height:93px;
    background:linear-gradient(var(--sky-top),var(--sky-bottom));display:flex;align-items:center;justify-content:center}
  .brand__name{color:var(--ink-light);font-size:24px;font-weight:700;letter-spacing:3px;text-transform:uppercase}

  .listings{position:absolute;left:14px;right:14px;top:275px;height:306px;background:var(--panel);
    display:flex;padding:0 3px}
  .listing{flex:1;position:relative;border-right:2px solid var(--divider);padding:15px 9px 0;
    color:var(--ink-light);text-align:center}
  .listing:last-child{border-right:none}
  .listing__photo{position:relative;width:114px;height:87px;margin:0 auto;border:2px solid #fff}
  .listing__price{position:absolute;right:-14px;bottom:-32px;width:60px;height:60px;border-radius:50%;
    background:var(--badge);border:3px solid var(--badge-ring);display:flex;align-items:center;justify-content:center;
    font-weight:700;font-size:17px;color:var(--ink-dark);text-align:center;line-height:1}
  .listing__price--range{font-size:12px;line-height:1.05}
  .listing__price--note{font-size:6.5px;font-weight:400;line-height:1.15;padding:0 5px}
  .listing__text{margin-top:44px;font-size:13px;line-height:1.25}
  .listing__text--lead{font-size:16px;line-height:1.3}
  .listing__text--small{font-size:11.5px;line-height:1.25}
</style>
</head>
<body>
  <article class="flyer">
    <div class="topbar"><span class="topbar__url">www.lodgio.com.au</span></div>
    <div class="hero" role="img" aria-label="Resort pool with palm trees on a grassy island and a colonnaded building behind"></div>
    <div class="brand"><span class="brand__name">Lodgio</span></div>

    <section class="listings">
      <div class="listing">
        <div class="listing__photo" role="img" aria-label="Two-storey timber house with a green lawn" style="background:linear-gradient(#b9c4c9,#6b5a45 55%,#5c8a3a)">
          <span class="listing__price">$1000</span>
        </div>
        <p class="listing__text listing__text--lead">Wattles Retreat is so different from anything else on offer in the South West, covering over 100 sq m.</p>
      </div>
      <div class="listing">
        <div class="listing__photo" role="img" aria-label="Bush cottage with veranda and umbrella on the lawn" style="background:linear-gradient(#d6dde0,#7c6a52 50%,#6f9a44)">
          <span class="listing__price">$350</span>
        </div>
        <p class="listing__text">Superbly quiet 5 acre bush location. No neighbours in view or ear shot. The property is only 10 minutes to Tarrabellup for shopping</p>
      </div>
      <div class="listing">
        <div class="listing__photo" role="img" aria-label="Bright open-plan studio living room" style="background:linear-gradient(#e4ddd2,#9a8570 60%,#5a4a3c)">
          <span class="listing__price">$300</span>
        </div>
        <p class="listing__text listing__text--small">Ferncliff Studio is a beautiful, rustic 2 bedroom cottage set amongst 30 acres of parklands and beautiful stands of marri bushland.</p>
      </div>
      <div class="listing">
        <div class="listing__photo" role="img" aria-label="Home with pergola and garden in front" style="background:linear-gradient(#9cc4e0,#6a5a46 50%,#4f7d34)">
          <span class="listing__price listing__price--note">A deposit bond is required as confirmation of your booking</span>
        </div>
        <p class="listing__text listing__text--small">Bellintary......or "care no more" has all you need for a relaxing and fun filled holiday. The quiet location at the end of a cul de sac is very secluded with no neighbours to be seen.</p>
      </div>
      <div class="listing">
        <div class="listing__photo" role="img" aria-label="Holiday home among trees with a wide lawn" style="background:linear-gradient(#a9cbe3,#7a6a50 45%,#5e9a3a)">
          <span class="listing__price listing__price--range">$200<br>to<br>$600</span>
        </div>
        <p class="listing__text">Quokkas Corner is a fantastic holiday home, only 10 mins to Tarrabellup and the beaches, but nestled ON 5 ACRES in a lovely quiet location.</p>
      </div>
      <div class="listing">
        <div class="listing__photo" role="img" aria-label="Timber deck with outdoor table and chairs" style="background:linear-gradient(#5f6a70,#8a7a64 55%,#a0876a)">
          <span class="listing__price">$500</span>
        </div>
        <p class="listing__text listing__text--small">This fabulous home is set on 3 acres just around the corner from Banksia Gallery, so walking there for their famous breakfast is a must during your holiday.</p>
      </div>
    </section>
  </article>
</body>
</html>
```